HarmoNest Ensemble Jubilee
Date: Sunday Oct 2, 2022
When: 2-4 p.m.
Location: Brindle9 Alehouse
413 Marlowe Ct #200, Sacramento, CA 95821
Tickets: www.Tixolvo.com
General seating: $15 for adults and $10 for students

```html
<!DOCTYPE html>
<html lang="en">
<head>
<meta charset="utf-8">
<title>HarmoNest Ensemble Jubilee</title>
<link rel="stylesheet" href="https://fonts.googleapis.com/css2?family=Great+Vibes&family=Cinzel:wght@400;600&family=Cormorant+SC:wght@500&family=Montserrat:ital,wght@1,800&family=Varela+Round&family=Roboto:ital,wght@1,700&display=swap">
<style>
  :root {
    --ink: #03070d;
    --ink-soft: #0a1520;
    --sky: #5fd3f0;
    --azure: #3a86e8;
    --cyan-band: #00b1d6;
    --slate: #1c2b36;
    --slate-deep: #142029;
    --label-bg: #1e3040;
    --text-light: #e6edf2;
    --rule: #2a6fb8;
  }
  * { box-sizing: border-box; margin: 0; padding: 0; }
  html, body { width: 800px; height: 1200px; overflow: hidden; background: var(--ink); }
  .flyer {
    position: relative; width: 800px; height: 1200px; overflow: hidden;
    background: radial-gradient(ellipse at 50% 55%, var(--ink-soft) 0%, var(--ink) 70%);
    color: var(--text-light);
  }
  .top-rule { position: absolute; top: 86px; left: 56px; right: 56px; height: 1px; background: var(--rule); }
  .flourish {
    position: absolute; top: 76px; left: 348px; width: 104px; height: 22px;
    background: var(--ink); display: flex; align-items: center; justify-content: center;
  }
  .flourish span { display: block; width: 84px; height: 12px; border-radius: 6px; background: linear-gradient(90deg, var(--azure), var(--sky)); opacity: .7; }
  .title-script {
    position: absolute; top: 122px; left: 0; width: 800px; text-align: center;
    font-family: "Great Vibes", cursive; font-size: 92px; line-height: 1;
    background: linear-gradient(90deg, var(--sky), var(--azure) 55%, var(--sky));
    -webkit-background-clip: text; background-clip: text; color: transparent;
  }
  .title-caps {
    position: absolute; top: 252px; left: 0; width: 800px; text-align: center;
    font-family: "Cinzel", serif; font-weight: 400; font-size: 62px; letter-spacing: 2px;
    color: var(--sky);
  }
  .title-rule { position: absolute; top: 350px; left: 208px; width: 384px; height: 1px; background: var(--rule); }
  .date {
    position: absolute; top: 368px; left: 0; width: 800px; text-align: center;
    font-family: "Cormorant SC", serif; font-weight: 500; font-size: 25px; color: var(--text-light);
  }
  .photo {
    position: absolute; top: 414px; left: 150px; width: 520px; height: 350px;
    background: radial-gradient(ellipse at 52% 55%, #6a3b3a 0%, #2a3e4c 38%, rgba(10,21,32,0) 72%);
  }
  .seating-label {
    position: absolute; top: 766px; left: 234px; width: 320px; height: 42px;
    background: var(--label-bg); text-align: center;
    font-family: "Cinzel", serif; font-weight: 600; font-size: 29px; line-height: 42px;
    color: var(--azure); letter-spacing: 1px;
  }
  .price-frame { position: absolute; top: 826px; left: 150px; width: 500px; height: 172px; }
  .price {
    position: absolute; top: 852px; width: 220px; text-align: center;
  }
  .price--adults { left: 195px; }
  .price--students { left: 400px; }
  .price-amount {
    font-family: "Montserrat", sans-serif; font-style: italic; font-weight: 800;
    font-size: 56px; line-height: 1.05; color: var(--sky);
  }
  .price-who { font-family: "Varela Round", sans-serif; font-size: 34px; line-height: 1.1; color: var(--text-light); }
  .footer-shapes { position: absolute; top: 1032px; left: 0; width: 800px; height: 168px; }
  .address {
    position: absolute; top: 1036px; left: 0; width: 800px; text-align: center;
    font-family: "Roboto", sans-serif; font-style: italic; font-weight: 700;
    font-size: 25px; line-height: 38px; color: var(--text-light);
  }
  .booking {
    position: absolute; top: 1144px; left: 0; width: 800px; text-align: center;
    font-family: "Roboto", sans-serif; font-style: italic; font-weight: 700;
    font-size: 21px; color: var(--sky);
  }
</style>
</head>
<body>
<main class="flyer">
  <div class="top-rule"></div>
  <div class="flourish" role="img" aria-label="Decorative scroll flourish"><span></span></div>

  <h1>
    <span class="title-script">HarmoNest Ensemble</span>
    <span class="title-caps">Jubilee</span>
  </h1>
  <div class="title-rule"></div>
  <p class="date">2-4 p.m. Sunday Oct 2, 2022</p>

  <div class="photo" role="img" aria-label="Photo of a female singer in a sequined top singing into a microphone, lit in red and teal, with faint music notes and a treble clef behind her"></div>

  <p class="seating-label">General seating:</p>

  <svg class="price-frame" viewBox="0 0 500 172" aria-hidden="true">
    <g fill="none" stroke="var(--azure)" stroke-width="1.5">
      <polyline points="185,6 40,6 4,86 40,166 205,166"/>
      <polyline points="315,6 460,6 496,86 460,166 295,166"/>
      <line x1="250" y1="28" x2="250" y2="144" stroke="var(--text-light)" stroke-width="1"/>
    </g>
    <rect x="205" y="0" width="90" height="12" rx="6" fill="var(--azure)" opacity=".6" role="img" aria-label="Small scroll ornament"/>
    <rect x="215" y="160" width="70" height="12" rx="6" fill="var(--azure)" opacity=".5" role="img" aria-label="Small scroll ornament"/>
  </svg>
  <div class="price price--adults">
    <div class="price-amount">$15</div>
    <div class="price-who">for adults</div>
  </div>
  <div class="price price--students">
    <div class="price-amount">$10</div>
    <div class="price-who">for students</div>
  </div>

  <svg class="footer-shapes" viewBox="0 0 800 168" preserveAspectRatio="none" aria-hidden="true">
    <rect x="0" y="0" width="800" height="92" fill="var(--cyan-band)"/>
    <polygon points="0,12 28,30 148,92 0,92" fill="var(--slate)"/>
    <polygon points="800,12 772,30 652,92 800,92" fill="var(--slate)"/>
    <polygon points="0,12 28,30 10,92 0,92" fill="var(--slate-deep)"/>
    <polygon points="800,12 772,30 790,92 800,92" fill="var(--slate-deep)"/>
    <rect x="0" y="92" width="800" height="76" fill="var(--slate)"/>
  </svg>
  <p class="address">Brindle9 Alehouse 413 Marlowe Ct #200,<br>Sacramento, CA 95821</p>
  <p class="booking">For booking visit the website: www.Tixolvo.com</p>
</main>
</body>
</html>
```